Modern Label for cleaning products for the brand Voralux

We need a label design for our line of cleaning products. The label should feature our logo and an image to identify the product's intended use. I've added our logo and an image for use. This only concerns the design of the label on the front of the bottle.

Label dimensions:
Label 1 (500ml bottle with spray): width 58mm x height 115mm
Label 2: (1L bottle): width 73mm x height 140mm
The design must be consistent for both bottles which you find in the pictures.

The bottles to be labeled are white. See the attachment for a photo of the bottles.

The photo must also appear on the label to identify the product's intended use.

Product information:
Brand: Voralux
Product: Sanitary Cleaner

This text must be placed on the label:
"Cleans, descales & freshens. followed with this text: "Ideal for quick and powerful cleaning. A ready-to-use product for everyday use."

- Mention the seperate USP's: Sanitary, Bathroom, Toilet, Wet areas

Appearance: This is a consumer product, but it must have a professional appearance. We would like to see a design that use the color blue from our logo.

Target Market(s)

Consumers who take care of their homes and want to maintain it the correct (professional) way

Font styles to use
Sans Serif

Colors
0054AA
0677BA
7BADD7
CADEEF
E8F1F8

Requirements
Must have
• USP's + use of image and logo + blend in 1 design
Nice to have
• Keep the color of the logo in the design
Should not have
• Comic sans

```html
<!DOCTYPE html>
<html lang="en">
<head>
<meta charset="utf-8">
<title>Voralux Sanitary Cleaner – Labels</title>
<link href="https://fonts.googleapis.com/css2?family=Montserrat:wght@400;500;600;700;800&display=swap" rel="stylesheet">
<style>
  :root{
    --navy:#0054AA;
    --ocean:#0677BA;
    --sky:#7BADD7;
    --mist:#CADEEF;
    --ice:#E8F1F8;
    --stage-left:#0152B8;
    --stage-right:#2B7EE3;
    --ink:#1b1b1f;
    --white:#ffffff;
  }
  *{box-sizing:border-box;margin:0;padding:0}
  html,body{width:1200px;height:589px;overflow:hidden}
  body{font-family:"Montserrat",Arial,sans-serif;display:flex}
  .stage{width:600px;height:589px;display:flex;align-items:center;justify-content:center}
  .stage--litre{background:var(--stage-left)}
  .stage--spray{background:var(--stage-right)}

  .label{position:relative;width:222px;height:428px;overflow:hidden;
    background:radial-gradient(ellipse at 0% 20%,var(--mist) 0%,rgba(202,222,239,0) 40%),
               radial-gradient(ellipse at 100% 0%,var(--sky) 0%,rgba(123,173,215,0) 42%),
               var(--white);
    box-shadow:0 4px 14px rgba(0,0,0,.18)}

  .brand{position:absolute;top:30px;left:0;right:0;text-align:center}
  .brand__dot{display:block;width:40px;height:40px;margin:0 auto 6px;border-radius:50%;background:var(--navy)}
  .brand__name{font-weight:700;font-size:20px;color:var(--ink);letter-spacing:.2px}

  .title{position:absolute;top:108px;left:0;width:222px;height:70px}
  .title__text{position:absolute;top:118px;left:48px;width:140px;color:var(--white);font-weight:800;font-size:22px;line-height:20px;text-align:center}
  .title__text span{display:block}
  .title__text span:last-child{padding-left:20px}

  .claim{position:absolute;top:174px;left:36px;width:152px;height:26px;border:2px solid var(--ocean);border-radius:4px;background:var(--white);
    display:flex;align-items:center;justify-content:center;color:var(--ocean);font-weight:700;font-size:9px;transform:rotate(-2deg)}

  .intro{position:absolute;top:214px;left:0;right:0;text-align:center;font-size:9px;line-height:13px;color:var(--ink)}

  .usps{position:absolute;top:250px;left:24px;right:20px;display:flex;justify-content:space-between}
  .usps__col{display:flex;flex-direction:column;gap:5px}
  .usps__col--right{border-left:1px solid var(--ink);padding-left:14px}
  .usp{display:flex;align-items:center;gap:6px;font-size:11px;color:var(--ink)}
  .usp svg{width:11px;height:11px;flex:none}

  .scene{position:absolute;left:0;bottom:0;width:222px;height:138px}
  .scene__photo{position:absolute;left:0;bottom:0;width:222px;height:118px;background:linear-gradient(180deg,var(--sky) 0%,var(--mist) 55%,#8fb1cf 100%)}
  .scene__wave{position:absolute;left:0;top:0;width:222px;height:50px}
  .volume{position:absolute;bottom:24px;left:50%;transform:translateX(-50%);background:var(--navy);color:var(--white);
    font-size:12px;font-weight:500;padding:3px 7px;border-radius:2px}
</style>
</head>
<body>

<section class="stage stage--litre">
  <article class="label">
    <div class="brand"><span class="brand__dot"></span><span class="brand__name">voralux</span></div>
    <svg class="title" viewBox="0 0 222 70" aria-hidden="true">
      <path d="M46 24 C60 4 150 -2 200 14 C214 22 208 42 190 54 C150 72 80 72 48 60 C36 52 38 36 46 24Z" fill="var(--ocean)"/>
      <path d="M56 22 C80 8 150 6 190 18" stroke="var(--sky)" stroke-width="3" fill="none" stroke-linecap="round"/>
    </svg>
    <div class="title__text"><span>Sanitary</span><span>Cleaner</span></div>
    <div class="claim">Cleans, Descales &amp; Freshens</div>
    <p class="intro">Ideal for quick and powerful cleaning.<br>A ready to use product for everyday use.</p>
    <div class="usps">
      <div class="usps__col">
        <div class="usp"><svg viewBox="0 0 12 12"><path d="M1 6h10v2a3 3 0 0 1-3 3H4a3 3 0 0 1-3-3z M5 2h2v3H5z" fill="var(--ocean)"/></svg>Sanitary</div>
        <div class="usp"><svg viewBox="0 0 12 12"><path d="M1 6h10v2a3 3 0 0 1-3 3H4a3 3 0 0 1-3-3z M2 1h2v5H2z" fill="var(--ocean)"/></svg>Bathroom</div>
      </div>
      <div class="usps__col usps__col--right">
        <div class="usp"><svg viewBox="0 0 12 12"><path d="M2 1h4v4H2z M2 6h8a3 3 0 0 1-3 3v2H4V9a2 2 0 0 1-2-2z" fill="var(--ocean)"/></svg>Toilet</div>
        <div class="usp"><svg viewBox="0 0 12 12"><path d="M6 0.5a4 4 0 0 1 4 4c0 3-4 7-4 7s-4-4-4-7a4 4 0 0 1 4-4z" fill="var(--ocean)"/><circle cx="6" cy="4.5" r="1.5" fill="var(--white)"/></svg>Wet areas</div>
      </div>
    </div>
    <div class="scene">
      <div class="scene__photo" role="img" aria-label="Photo of a bright modern bathroom with glass shower and bathtub"></div>
      <svg class="scene__wave" viewBox="0 0 222 50" preserveAspectRatio="none" aria-hidden="true">
        <path d="M0 14 C60 -4 110 30 222 16 V30 C120 44 60 20 0 34Z" fill="var(--ocean)"/>
        <path d="M0 20 C60 4 110 36 222 24 V40 C120 50 60 28 0 40Z" fill="var(--sky)" opacity=".7"/>
      </svg>
      <span class="volume">1L</span>
    </div>
  </article>
</section>

<section class="stage stage--spray">
  <article class="label">
    <div class="brand"><span class="brand__dot"></span><span class="brand__name">voralux</span></div>
    <svg class="title" viewBox="0 0 222 70" aria-hidden="true">
      <path d="M46 24 C60 4 150 -2 200 14 C214 22 208 42 190 54 C150 72 80 72 48 60 C36 52 38 36 46 24Z" fill="var(--ocean)"/>
      <path d="M56 22 C80 8 150 6 190 18" stroke="var(--sky)" stroke-width="3" fill="none" stroke-linecap="round"/>
    </svg>
    <div class="title__text"><span>Sanitary</span><span>Cleaner</span></div>
    <div class="claim">Cleans, Descales &amp; Freshens</div>
    <p class="intro">Ideal for quick and powerful cleaning.<br>A ready to use product for everyday use.</p>
    <div class="usps">
      <div class="usps__col">
        <div class="usp"><svg viewBox="0 0 12 12"><path d="M1 6h10v2a3 3 0 0 1-3 3H4a3 3 0 0 1-3-3z M5 2h2v3H5z" fill="var(--ocean)"/></svg>Sanitary</div>
        <div class="usp"><svg viewBox="0 0 12 12"><path d="M1 6h10v2a3 3 0 0 1-3 3H4a3 3 0 0 1-3-3z M2 1h2v5H2z" fill="var(--ocean)"/></svg>Bathroom</div>
      </div>
      <div class="usps__col usps__col--right">
        <div class="usp"><svg viewBox="0 0 12 12"><path d="M2 1h4v4H2z M2 6h8a3 3 0 0 1-3 3v2H4V9a2 2 0 0 1-2-2z" fill="var(--ocean)"/></svg>Toilet</div>
        <div class="usp"><svg viewBox="0 0 12 12"><path d="M6 0.5a4 4 0 0 1 4 4c0 3-4 7-4 7s-4-4-4-7a4 4 0 0 1 4-4z" fill="var(--ocean)"/><circle cx="6" cy="4.5" r="1.5" fill="var(--white)"/></svg>Wet areas</div>
      </div>
    </div>
    <div class="scene">
      <div class="scene__photo" role="img" aria-label="Photo of a bright modern bathroom with glass shower and bathtub"></div>
      <svg class="scene__wave" viewBox="0 0 222 50" preserveAspectRatio="none" aria-hidden="true">
        <path d="M0 14 C60 -4 110 30 222 16 V30 C120 44 60 20 0 34Z" fill="var(--ocean)"/>
        <path d="M0 20 C60 4 110 36 222 24 V40 C120 50 60 28 0 40Z" fill="var(--sky)" opacity=".7"/>
      </svg>
      <span class="volume">500 ml</span>
    </div>
  </article>
</section>

</body>
</html>
```